Vrano = Difficult

Sto Je Treba Ni Vrano
what must be done, is not difficult...

my mom is Croatian and her name is Ranka.

a Croatian expression that I came across 12 years ago is 'what must be done, is not difficult'. yes, it is counter-intuitive. but it helped me to get divorced and then to beat Stage 4 cancer. both seem impossible,

but they they had to be done, so they were not difficult.

so I have started up a new company called:
Vrano Consulting - solving difficult

I'll be working with companies that have a difficult program/project that they haven't launched yet...

I envision possibly a business card that is shaped into a "D" to represent the Croatian word of difficult.

yes, I know this is difficult - welcome to my new world - the difficult challenges are worth solving...

a nod to the red/white design of the Croatian flag would be nice.

```html
<!DOCTYPE html>
<html lang="en">
<head>
<meta charset="utf-8">
<title>Vrano Consulting – Business Card</title>
<link href="https://fonts.googleapis.com/css2?family=Cormorant+Garamond:wght@500&family=Poiret+One&display=swap" rel="stylesheet">
<style>
  :root {
    --backdrop: #d6d6d6;
    --flag-red: #ec2227;
    --flag-white: #ffffff;
    --flag-navy: #24265e;
    --frame-silver: #a9a9ab;
    --frame-light: #e8e8ea;
    --crest-tint: #f6e3e4;
    --label-ink: #3b4677;
  }
  html, body {
    margin: 0;
    padding: 0;
    width: 1200px;
    height: 900px;
    overflow: hidden;
    background: var(--backdrop);
  }
  .presentation {
    display: block;
    width: 1200px;
    height: 900px;
  }
  .band-red { fill: var(--flag-red); }
  .band-white { fill: var(--flag-white); }
  .band-navy { fill: var(--flag-navy); }
  .card-frame-outer { fill: none; stroke: var(--frame-silver); stroke-width: 8; }
  .card-frame-inner { fill: none; stroke: var(--frame-light); stroke-width: 3; }
  .crest-area { fill: var(--crest-tint); opacity: 0.6; }
  .tagline {
    font-family: "Cormorant Garamond", serif;
    font-weight: 500;
    fill: var(--flag-white);
  }
  .tagline-top { font-size: 30px; letter-spacing: 4px; }
  .tagline-bottom { font-size: 32px; letter-spacing: 9px; }
  .wordmark {
    font-family: "Poiret One", sans-serif;
    fill: var(--flag-red);
    font-weight: 400;
  }
  .wordmark-name { font-size: 128px; }
  .wordmark-descriptor { font-size: 58px; }
  .holder-name {
    font-family: "Poiret One", sans-serif;
    font-size: 46px;
    fill: var(--flag-red);
  }
  .contact-line {
    font-family: "Poiret One", sans-serif;
    font-size: 30px;
    fill: var(--flag-navy);
  }
  .side-label {
    font-family: "Poiret One", sans-serif;
    font-size: 27px;
    letter-spacing: 15px;
    fill: var(--label-ink);
  }
</style>
</head>
<body>
<svg class="presentation" viewBox="0 0 1200 900" xmlns="http://www.w3.org/2000/svg">
  <defs>
    <clipPath id="front-shape">
      <path d="M92,35 H220 A340,396.5 0 0 1 220,828 H92 Z"/>
    </clipPath>
    <clipPath id="back-shape">
      <path d="M1103,40 H980 A340,391.5 0 0 0 980,823 H1103 Z"/>
    </clipPath>
  </defs>

  <!-- Front of card -->
  <g class="card card-front">
    <g clip-path="url(#front-shape)">
      <rect class="band-red" x="80" y="30" width="500" height="237"/>
      <rect class="band-white" x="80" y="267" width="500" height="321"/>
      <rect class="band-navy" x="80" y="588" width="500" height="245"/>
    </g>
    <path class="card-frame-outer" d="M92,35 H220 A340,396.5 0 0 1 220,828 H92 Z"/>
    <path class="card-frame-inner" d="M92,35 H220 A340,396.5 0 0 1 220,828 H92 Z"/>

    <text class="tagline tagline-top" x="128" y="252">it's close to the intent.</text>

    <text class="wordmark" x="322" y="0" text-anchor="middle">
      <tspan class="wordmark-name" x="322" y="448">vrano</tspan>
      <tspan class="wordmark-descriptor" x="322" y="506">consulting</tspan>
    </text>

    <text class="tagline tagline-bottom" x="135" y="626">solving difficult</text>
  </g>

  <!-- Back of card -->
  <g class="card card-back">
    <g clip-path="url(#back-shape)">
      <rect class="band-red" x="620" y="35" width="500" height="235"/>
      <rect class="band-white" x="620" y="270" width="500" height="321"/>
      <rect class="band-navy" x="620" y="591" width="500" height="240"/>
    </g>
    <path class="card-frame-outer" d="M1103,40 H980 A340,391.5 0 0 0 980,823 H1103 Z"/>
    <path class="card-frame-inner" d="M1103,40 H980 A340,391.5 0 0 0 980,823 H1103 Z"/>

    <path class="crest-area" role="img" aria-label="Faint red and white checkered shield emblem behind the contact details"
          d="M790,300 H975 V470 A92.5,110 0 0 1 790,470 Z"/>

    <text class="holder-name" x="880" y="342" text-anchor="middle">Dale Morrow</text>
    <text class="contact-line" x="880" y="409" text-anchor="middle">217 Linden Avenue</text>
    <text class="contact-line" x="880" y="454" text-anchor="middle">Marlow, GA 30412</text>
    <text class="contact-line" x="880" y="499" text-anchor="middle">555-210-4836</text>
    <text class="contact-line" x="880" y="546" text-anchor="middle">dale@vranoconsulting.com</text>
  </g>

  <text class="side-label" x="94" y="875">Front Side</text>
  <text class="side-label" x="840" y="880">Back Side</text>
</svg>
</body>
</html>
```